vermalo web design

- Company / Site Description
We are developing a website that will allow anyone in Europe to find in one click, cultural things to do (Exhibition, Museum, Monument, Zoo, Aquarium, Archaeological site…) with friends or family, and to organize the visit (book a ticket / a private visit, book a restaurant nearby…).

Examples
1. You're in London with your girlfriend, it's saturday 10 am, you have two hours to spend and you want to see an exhibition. We provide you in one click all the exhibition matching your location / time and date.

2. You're in Berlin with some friends, it's thursday night you want to go out, but you don't know what to do. We provide you a list of experience, you can select for instance "I want to be on top of the world", and we show you a list of venues matching the selected experience / date / time /location of your request.

- Brand name : Vermalo
- Activity : Cultural Leisure, cultural entertainment

- Target audience
Broad target will be between 20 and 55. Core target will be between 25 and 40. Most likely to live in a city and in Europe.

- Behaviours and preferences
Our user is under time constraint (few minutes to find and choose his visit), idea constraint (is not sure about what to do and see) and money constraint.
He wants to have an easy to use website, not cluttered with information, focussed on added value information. He wants to have a website which is modern, fun and elegant that he will deem as professional and trustworthy.

- Our expectations (Do’s and Don’t)
We want to move away from traditional design. We want some OUT OF THE BOX design. Think of a website design that will look like an app design.
We want to make an awesome / extra ordinary /remember-able design. The design must be so cool, that the user wants to come back to the site. In two words: THINK EXTRAORDINARY.
You can use photos to help the user understand functions. If you use photo, use creative commons license photo.
Avoid black colors

- Functional Requirements
We need Four pages:
1. Home Page (desktop and mobile version): it’s both the homepage and the assistant page. This page will allow the user to find in one click his visit (please refer to the pdf file Assistant home page). The page must be self-explanatory for a first time user.
2. Assistant result page (desktop version): it’s the page that display the results found by the assistant based on the criteria search (please refer to the pdf file mockup - Assistant result page)
3. Site / Event page (desktop version): it’s the page that display each result information (please refer to the pdf file mockup – Event / Site Page)
The pdf files list all the elements include in each page + gives you a mockup of each page (just to put in perspective the element required). You are completely free about the design.
We don’t have the logo yet. Use a dummy logo for your page design.
The selected winner can expect to work with us immediately after the contest and on a on a regular basis later on.

- Technical Requirements
No Flash
For the winner, we will manage the CSS you will just need to provide :
. One PSD file containing all the pages
. Inside the PSD file we want for each page two groups: the first group will embed the desktop design, the second group will embed the responsive mobile design (Home Page only).
In total there should be 4 groups inside the PSD file (3 desktop groups, 1 mobile group).
Each group must contain all the elements specified in the pdf file

Website we like
http://demo.plandorix.example/?theme=Velunt
http://rosabel.quintorhub.example/#home
http://blogsite.fenk.daltoroute.example/2/
http://demo.plandorix.example/?theme=Mosaru
http://www.quarnivo.example/themes/lumbe/
http://gridmarket.example/item/tav-responsive-photography-blog-theme/full_screen_preview/8146027
http://items.zkvortel.example/?product=example
http://uk.harnoway.example

Reason: Due to the request of several designers, we have agreed to add 7 additional days to the contest deadline. Thank you. The vermalo team

Reason: We still need to collect all the votes. Sorry for the delay.

Reason: Hello, We extend the contest deadline, in order to collect all the votes from the poll. We should have everything finalized by sunday. Thank you vermalo team

```html
<!DOCTYPE html>
<html lang="en">
<head>
<meta charset="utf-8">
<title>Vermalo – My Assistant</title>
<link href="https://fonts.googleapis.com/css2?family=Montserrat:wght@300;400;600;700&family=Raleway:wght@100;300;400&display=swap" rel="stylesheet">
<style>
  :root {
    --bar: #27262b;
    --bar-text: #e6e6e6;
    --tab: #fdd0b2;
    --coral: #f47a6f;
    --ink: #1e1e22;
    --navy-text: #33327a;
    --row-date: #ffdfb5;
    --row-time: #ffcdb3;
    --row-place: #ffb3b5;
    --row-want: #3651a4;
    --go: #2a3d8f;
    --tick: #b59aa6;
    --white: #ffffff;
  }
  * { box-sizing: border-box; margin: 0; padding: 0; }
  html, body { width: 1200px; height: 954px; overflow: hidden; }
  body { position: relative; font-family: "Montserrat", sans-serif; background: var(--white); color: var(--ink); }

  .top-bar { position: absolute; left: 0; top: 0; width: 1200px; height: 41px; background: var(--bar); }
  .tab { position: absolute; top: 0; height: 41px; display: flex; align-items: center; justify-content: center; font-size: 12px; letter-spacing: .5px; text-transform: uppercase; color: #bdbdc2; }
  .tab--active { left: 162px; width: 212px; background: var(--tab); color: var(--ink); font-weight: 600; }
  .tab--active::after { content: ""; position: absolute; left: 94px; top: 41px; border: 8px solid transparent; border-top: 8px solid var(--tab); }
  .tab--favourites { left: 420px; width: 140px; font-weight: 400; }
  .search { position: absolute; left: 860px; top: 12px; font-size: 12px; color: var(--bar-text); display: flex; align-items: center; gap: 14px; }
  .bar-divider { position: absolute; left: 947px; top: 0; width: 1px; height: 41px; background: #48474d; }
  .login { position: absolute; left: 967px; top: 8px; font-size: 12px; color: var(--bar-text); display: flex; align-items: center; gap: 18px; }

  .intro-panel { position: absolute; left: 0; top: 41px; width: 600px; height: 870px; background: var(--white); }
  .headline { position: absolute; left: 161px; top: 60px; font-family: "Raleway", sans-serif; font-weight: 100; font-size: 48px; letter-spacing: -1px; color: var(--ink); white-space: nowrap; }
  .headline strong { font-weight: 400; color: var(--coral); }
  .subline { position: absolute; right: 23px; top: 117px; font-size: 13px; font-weight: 400; color: var(--ink); }
  .tagline { position: absolute; right: 21px; top: 149px; font-size: 11.5px; font-weight: 700; color: var(--coral); letter-spacing: .3px; }

  .photo { position: absolute; }
  .photo--sculpture { left: 163px; top: 221px; width: 206px; height: 167px; background: linear-gradient(160deg, #eef0f1, #b9bcbf 60%, #8e9194); }
  .photo--tiger { left: 163px; top: 388px; width: 206px; height: 109px; background: linear-gradient(90deg, #07073a 0 56%, #3a3a48 70%, #c8c8c8 85%, #5a5a62); }
  .photo--carousel { left: 163px; top: 497px; width: 206px; height: 154px; background: linear-gradient(160deg, #d9b28a, #b77a55 50%, #7a4a3a); }
  .photo--tower { left: 369px; top: 221px; width: 232px; height: 464px; background: linear-gradient(180deg, #1c1c55 0%, #2d2f78 35%, #8a7a58 62%, #3a4a2c 80%, #1c2418 100%); }

  .assistant-panel { position: absolute; left: 600px; top: 41px; width: 600px; height: 870px;
    background:
      radial-gradient(ellipse 380px 260px at 420px 20px, rgba(10,30,80,.55), transparent 70%),
      linear-gradient(180deg, #1e4c9e 0%, #3472c0 22%, #6ea2d8 42%, #b9c2cc 58%, #c89c98 70%, #9a5f72 84%, #3e2b55 100%);
    box-shadow: -4px 0 6px rgba(0,0,0,.45); }

  .weather { position: absolute; left: 372px; top: 48px; text-align: center; color: var(--white); }
  .weather__temp { font-size: 33px; font-weight: 700; margin-top: 4px; letter-spacing: -1px; }
  .weather__temp span { font-weight: 300; font-size: 24px; vertical-align: 6px; }

  .criteria { position: absolute; left: 63px; top: 225px; }
  .criterion { position: relative; display: flex; height: 76px; box-shadow: 1px 2px 4px rgba(0,0,0,.3); }
  .criterion__check { width: 72px; display: flex; align-items: center; justify-content: center; border-right: 1px solid rgba(0,0,0,.12); }
  .criterion__value { display: flex; align-items: center; padding-left: 24px; font-size: 19px; color: var(--navy-text); text-transform: uppercase; font-weight: 400; }
  .criterion__value b { font-weight: 700; margin-right: 6px; }
  .criterion--date { width: 377px; background: var(--row-date); }
  .criterion--time { width: 281px; background: var(--row-time); height: 75px; }
  .criterion--time .criterion__value { font-size: 30px; font-weight: 300; padding-left: 28px; }
  .criterion--place { width: 342px; background: var(--row-place); }
  .criterion--want { width: 377px; background: var(--row-want); height: 75px; }
  .criterion--want .criterion__check { font-size: 22px; font-weight: 700; color: var(--white); border-right-color: rgba(0,0,0,.25); align-items: flex-start; padding-top: 20px; }
  .criterion--want .criterion__value { color: var(--white); font-weight: 700; }

  .go-button { position: absolute; left: 372px; top: 555px; width: 72px; height: 72px; border-radius: 50%; background: var(--go); color: var(--white); display: flex; align-items: center; justify-content: center; gap: 3px; font-size: 18px; font-weight: 700; box-shadow: 1px 2px 4px rgba(0,0,0,.35); }

  .bottom-bar { position: absolute; left: 0; top: 911px; width: 1200px; height: 43px; background: var(--bar); color: var(--white); font-size: 12.5px; }
  .language { position: absolute; left: 88px; top: 11px; }
  .language strong { color: var(--tab); margin-left: 8px; font-weight: 600; }
  .plus { position: absolute; left: 984px; top: 14px; display: flex; align-items: center; gap: 6px; }
</style>
</head>
<body>
  <header class="top-bar">
    <nav>
      <div class="tab tab--active">My assistant</div>
      <div class="tab tab--favourites">My favourites</div>
    </nav>
    <div class="search">search
      <svg width="18" height="18" viewBox="0 0 18 18"><circle cx="6.5" cy="6.5" r="4.5" fill="none" stroke="#e6e6e6" stroke-width="2"/><line x1="10" y1="10" x2="16" y2="16" stroke="#e6e6e6" stroke-width="3" stroke-linecap="round"/></svg>
    </div>
    <div class="bar-divider"></div>
    <div class="login">login
      <svg width="24" height="24" viewBox="0 0 24 24"><circle cx="12" cy="12" r="11" fill="none" stroke="#e6e6e6" stroke-width="2"/><circle cx="12" cy="9" r="4" fill="#e6e6e6"/><path d="M4.5 19.5c2-4 13-4 15 0" fill="#e6e6e6"/></svg>
    </div>
  </header>

  <main>
    <section class="intro-panel">
      <h1 class="headline">FIND IN <strong>ONE</strong> CLICK</h1>
      <p class="subline">Exhibitions, museums, monuments, zoos...</p>
      <p class="tagline">TELL US WHAT YOU LIKE, WE WILL TELL YOU WHERE TO GO!</p>
      <div class="photo photo--sculpture" role="img" aria-label="Photo of a white marble sculpture"></div>
      <div class="photo photo--tiger" role="img" aria-label="Black and white photo of a tiger"></div>
      <div class="photo photo--carousel" role="img" aria-label="Photo of children riding a carousel"></div>
      <div class="photo photo--tower" role="img" aria-label="Night photo of the Eiffel Tower lit up"></div>
    </section>

    <section class="assistant-panel">
      <div class="weather">
        <svg width="60" height="56" viewBox="0 0 60 56" fill="none" stroke="#fff" stroke-width="3" stroke-linecap="round">
          <circle cx="40" cy="16" r="7"/>
          <line x1="40" y1="2" x2="40" y2="5"/><line x1="51" y1="7" x2="49" y2="9"/><line x1="55" y1="17" x2="52" y2="17"/>
          <path d="M12 40h36a8 8 0 0 0 0-16 12 12 0 0 0-22-3 9 9 0 0 0-14 6 7 7 0 0 0 0 13z" fill="#fff" stroke="#fff"/>
          <path d="M13 40h34" stroke="#3a6fbd" stroke-width="2"/>
          <line x1="20" y1="47" x2="20" y2="48"/><line x1="28" y1="49" x2="28" y2="50"/><line x1="36" y1="47" x2="36" y2="48"/><line x1="44" y1="49" x2="44" y2="50"/><line x1="24" y1="54" x2="24" y2="55"/><line x1="32" y1="54" x2="32" y2="55"/>
        </svg>
        <div class="weather__temp">16<span>°C</span></div>
      </div>

      <div class="criteria">
        <div class="criterion criterion--date">
          <div class="criterion__check"><svg width="24" height="18" viewBox="0 0 24 18"><path d="M2 9l7 7L22 2" fill="none" stroke="var(--tick)" stroke-width="3"/></svg></div>
          <div class="criterion__value"><b>Saturday 14</b> December</div>
        </div>
        <div class="criterion criterion--time">
          <div class="criterion__check"><svg width="24" height="18" viewBox="0 0 24 18"><path d="M2 9l7 7L22 2" fill="none" stroke="var(--tick)" stroke-width="3"/></svg></div>
          <div class="criterion__value">11:00</div>
        </div>
        <div class="criterion criterion--place">
          <div class="criterion__check"><svg width="24" height="18" viewBox="0 0 24 18"><path d="M2 9l7 7L22 2" fill="none" stroke="var(--tick)" stroke-width="3"/></svg></div>
          <div class="criterion__value"><b>Paris</b> France</div>
        </div>
        <div class="criterion criterion--want">
          <div class="criterion__check">?</div>
          <div class="criterion__value">You want</div>
        </div>
      </div>

      <div class="go-button">GO
        <svg width="8" height="12" viewBox="0 0 8 12"><path d="M0 0l8 6-8 6z" fill="#fff"/></svg>
      </div>
    </section>
  </main>

  <footer class="bottom-bar">
    <div class="language">LANGUAGE <strong>english</strong></div>
    <div class="plus">PLUS
      <svg width="14" height="10" viewBox="0 0 14 10"><path d="M0 0h14L7 10z" fill="#fff"/></svg>
    </div>
  </footer>
</body>
</html>
```